Playvora Print Ad Design

Need a newspaper ad of size 24 cm H X 16 cm W for my toy rental library- Playvora

Toy Libraries are a new concept in India & so consumers need to be introduced to this concept through the ad.

The ad should communicate the following things

1. Why buy toys when you can rent a new one every week?
2. Our large collection of toys, games & puzzles (1000+ items)
3. Our collection is based on the Multiple Intelligence Theory of Dr. Leonard Whitcombe which says there are 8 intelligence areas.
4. Customers have the convenience of ordering online & getting home delivery or they could simply walk into to our library to borrow toys.

Please check our website www.playvorakids.in for more details of our service.

Rakesh

Target Market(s)

Parents of children in the age group 1 year - 7 years

Industry/Entity Type

Library

Requirements
Must have
• Photos or icons of toys, children playing etc

Different icons depicting the 8 intelligence areas

Our physical address
2nd Floor, 217 Sunmeadow Arcade, Opp Lotus Bazaar
Amberwood Phase-2, Gurgaon-122017

```html
<!DOCTYPE html>
<html lang="en">
<head>
<meta charset="utf-8">
<title>Playvora – Toy Rental Library</title>
<link rel="stylesheet" href="https://fonts.googleapis.com/css2?family=Lilita+One&family=Roboto+Condensed:wght@400;700&family=Roboto:wght@700&family=Jost:wght@400;500&family=Kalam:wght@700&display=swap">
<style>
  :root {
    --sky: #8ea7d3;
    --bubble-ring: #b9c9e6;
    --bubble-core: #5b82c4;
    --brand-purple: #6b3e91;
    --brand-teal: #2aa3cc;
    --ink: #1a1a1a;
    --ink-soft: #333333;
    --headline: #0d4ea6;
    --headline-dark: #0a3a80;
    --callout: #f7931e;
    --panel-blue: #4b73b9;
    --frame: #8aa6d6;
    --promo-red: #b3131c;
    --footer-top: #5b82c2;
    --footer-bottom: #4a71b4;
    --white: #ffffff;
    --icon-blue: #1f63b0;
    --icon-red: #d7232f;
    --icon-green: #1d9446;
    --icon-orange: #f0a22e;
    --icon-yellow: #f2c12e;
  }
  * { box-sizing: border-box; margin: 0; padding: 0; }
  html, body { width: 800px; height: 1200px; overflow: hidden; background: var(--white); }
  .ad { position: relative; width: 800px; height: 1200px; overflow: hidden; background: var(--white); font-family: "Roboto Condensed", Arial, sans-serif; }

  .sky { position: absolute; left: 0; top: 0; width: 800px; height: 140px; }

  .brand { position: absolute; left: 106px; top: 126px; }
  .brand-name { font-family: "Jost", Arial, sans-serif; font-weight: 500; font-size: 46px; line-height: 1; color: var(--brand-purple); margin-left: 24px; }
  .brand-tag { font-family: "Jost", Arial, sans-serif; font-weight: 500; font-size: 21px; color: var(--brand-teal); margin: 2px 0 0 28px; }
  .brand-theory { font-family: "Jost", Arial, sans-serif; font-size: 13px; color: var(--ink-soft); margin-top: 3px; }

  .hero-photo { position: absolute; left: 20px; top: 236px; width: 520px; height: 372px;
    background:
      radial-gradient(ellipse 110px 80px at 300px 300px, rgba(244,196,38,0.75), rgba(244,196,38,0) 100%),
      radial-gradient(ellipse 90px 70px at 420px 300px, rgba(226,45,40,0.65), rgba(226,45,40,0) 100%),
      radial-gradient(ellipse 80px 70px at 180px 270px, rgba(60,170,70,0.55), rgba(60,170,70,0) 100%),
      radial-gradient(ellipse 150px 110px at 150px 190px, rgba(246,214,90,0.85), rgba(246,214,90,0) 100%),
      radial-gradient(ellipse 130px 90px at 150px 300px, rgba(205,40,40,0.55), rgba(205,40,40,0) 100%),
      radial-gradient(ellipse 90px 90px at 160px 80px, rgba(240,196,166,0.95), rgba(240,196,166,0) 100%),
      radial-gradient(ellipse at 40% 50%, #f6e7d8 0%, #fbf6f1 55%, var(--white) 80%); }

  .headline { position: absolute; right: 46px; top: 256px; text-align: right; font-family: "Lilita One", "Arial Black", sans-serif; font-weight: 400; color: var(--headline); line-height: 1; }
  .headline-main { font-size: 72px; letter-spacing: 1px; }
  .headline-main .qmark { color: var(--headline-dark); font-size: 92px; }
  .headline-sub { font-size: 50px; letter-spacing: 1.5px; margin-top: 2px; }

  .callout { position: absolute; left: 492px; top: 460px; width: 280px; height: 90px; background: var(--callout); border-radius: 14px;
    color: var(--white); font-family: "Roboto", Arial, sans-serif; font-weight: 700; font-size: 19px; letter-spacing: 0.6px; line-height: 1.25; text-align: center; padding-top: 9px; }
  .callout-pointer { position: absolute; left: 446px; top: 474px; width: 60px; height: 30px; }

  .areas-frame { position: absolute; left: 20px; top: 660px; width: 762px; height: 270px; border: 4px solid var(--frame); border-radius: 22px; }
  .areas-title { position: absolute; left: 64px; top: 624px; width: 682px; height: 86px; background: var(--panel-blue); border-radius: 12px;
    color: var(--white); font-weight: 700; font-size: 25px; line-height: 1.3; text-align: center; padding-top: 12px; }

  .area { position: absolute; display: flex; align-items: center; }
  .area-icon { width: 76px; height: 64px; flex: none; margin-right: 12px; }
  .area-label { font-weight: 700; font-size: 15.5px; line-height: 1.4; color: var(--ink); }

  .promo { position: absolute; left: 0; top: 968px; width: 800px; text-align: center; font-family: "Kalam", cursive; font-weight: 700;
    font-size: 24px; line-height: 1.38; color: var(--promo-red); }

  .footer { position: absolute; left: 0; top: 1058px; width: 800px; height: 142px; background: linear-gradient(var(--footer-top), var(--footer-bottom));
    color: var(--white); text-align: center; }
  .footer-address { font-weight: 700; font-size: 17px; margin-top: 37px; }
  .footer-web { font-weight: 700; font-size: 44px; margin-top: 6px; }
</style>
</head>
<body>
<main class="ad">
  <svg class="sky" viewBox="0 0 800 140" aria-hidden="true">
    <rect width="800" height="140" fill="var(--sky)"/>
    <path d="M0 140 V96 C40 70 90 72 120 86 C150 20 260 10 300 60 C330 30 380 40 400 74 C440 50 500 60 520 90 C560 70 620 78 650 100 C690 80 760 90 800 110 V140 Z" fill="var(--white)"/>
    <circle cx="470" cy="38" r="12" fill="var(--white)"/>
    <circle cx="398" cy="102" r="22" fill="var(--bubble-ring)"/>
    <circle cx="398" cy="102" r="12" fill="var(--bubble-core)"/>
    <circle cx="645" cy="112" r="28" fill="var(--white)"/>
    <circle cx="645" cy="112" r="13" fill="var(--bubble-core)"/>
    <circle cx="730" cy="118" r="5" fill="var(--white)"/>
  </svg>

  <header class="brand">
    <div class="brand-name">Playvora</div>
    <div class="brand-tag">Toy Rental Library</div>
    <div class="brand-theory">Based on Multiple Intelligence Theory</div>
  </header>

  <div class="hero-photo" role="img" aria-label="Photo of a toddler in a yellow shirt sitting and playing with colourful toy building blocks"></div>

  <h1 class="headline">
    <div class="headline-main">Why buy toys<span class="qmark">?</span></div>
    <div class="headline-sub">when you can rent</div>
    <div class="headline-sub">a new one every week</div>
  </h1>

  <svg class="callout-pointer" viewBox="0 0 60 30" aria-hidden="true">
    <path d="M0 14 L60 0 L60 30 Z" fill="var(--callout)"/>
  </svg>
  <div class="callout">Large collection of<br>toys, games &amp; puzzles<br>(1000+ items)</div>

  <div class="areas-frame"></div>
  <h2 class="areas-title">Toys including 8 intelligence areas based on<br>Dr. Leonard Whitcombe‘s Multiple Intelligence Theory.</h2>

  <div class="area" style="left:50px;top:738px">
    <svg class="area-icon" viewBox="0 0 76 64" role="img" aria-label="Open book icon">
      <path d="M4 10 Q20 4 36 12 V60 Q20 52 4 56 Z" fill="var(--icon-blue)"/>
      <path d="M72 10 Q56 4 40 12 V60 Q56 52 72 56 Z" fill="var(--icon-blue)"/>
      <path d="M10 18 Q20 15 30 20 M10 28 Q20 25 30 30 M46 20 Q56 15 66 18 M46 30 Q56 25 66 28" stroke="#ffffff" stroke-width="2" fill="none" opacity="0.5"/>
    </svg>
    <div class="area-label">Linguistic<br>intelligence</div>
  </div>
  <div class="area" style="left:232px;top:740px">
    <svg class="area-icon" viewBox="0 0 76 64" role="img" aria-label="Maths symbols icon">
      <text x="38" y="46" text-anchor="middle" font-family="Roboto, Arial, sans-serif" font-weight="700" font-size="34" fill="var(--icon-blue)">÷%≤</text>
    </svg>
    <div class="area-label">Logical-<br>mathematical<br>intelligence</div>
  </div>
  <div class="area" style="left:418px;top:740px">
    <svg class="area-icon" viewBox="0 0 76 64" role="img" aria-label="Hand print icon">
      <g fill="var(--icon-red)">
        <rect x="20" y="26" width="34" height="32" rx="12"/>
        <rect x="20" y="8" width="8" height="28" rx="4"/>
        <rect x="29" y="4" width="8" height="30" rx="4"/>
        <rect x="38" y="5" width="8" height="30" rx="4"/>
        <rect x="47" y="10" width="7" height="26" rx="3.5"/>
        <rect x="6" y="30" width="8" height="22" rx="4" transform="rotate(-40 10 41)"/>
      </g>
    </svg>
    <div class="area-label">Bodily-<br>Kinesthetic<br>intelligence</div>
  </div>
  <div class="area" style="left:598px;top:738px">
    <svg class="area-icon" viewBox="0 0 76 64" role="img" aria-label="Music notes icon" style="width:66px">
      <text x="33" y="54" text-anchor="middle" font-family="Arial, sans-serif" font-size="60" fill="var(--icon-green)">♫</text>
    </svg>
    <div class="area-label">Musical<br>intelligence</div>
  </div>

  <div class="area" style="left:50px;top:834px">
    <svg class="area-icon" viewBox="0 0 76 64" role="img" aria-label="Two people icon">
      <g fill="var(--icon-orange)">
        <circle cx="22" cy="12" r="8"/>
        <path d="M10 24 H34 L30 42 H26 V62 H18 V42 H14 Z"/>
        <circle cx="54" cy="12" r="8"/>
        <path d="M42 24 H66 L62 42 H58 V62 H50 V42 H46 Z"/>
      </g>
    </svg>
    <div class="area-label">Interpersonal<br>intelligence</div>
  </div>
  <div class="area" style="left:232px;top:834px">
    <svg class="area-icon" viewBox="0 0 76 64" role="img" aria-label="Tree icon">
      <g fill="var(--icon-yellow)">
        <circle cx="38" cy="18" r="14"/>
        <circle cx="22" cy="24" r="9"/>
        <circle cx="54" cy="24" r="9"/>
        <rect x="34" y="28" width="8" height="34" rx="2"/>
        <circle cx="12" cy="8" r="3"/><circle cx="64" cy="8" r="3"/><circle cx="20" cy="4" r="2"/><circle cx="58" cy="2" r="2"/>
      </g>
    </svg>
    <div class="area-label">Intrapersonal<br>intelligence</div>
  </div>
  <div class="area" style="left:418px;top:834px">
    <svg class="area-icon" viewBox="0 0 76 64" role="img" aria-label="Leaf icon">
      <path d="M38 2 L46 16 L60 10 L56 26 L70 30 L56 40 L60 50 L42 46 L40 62 H36 L34 46 L16 50 L20 40 L6 30 L20 26 L16 10 L30 16 Z" fill="var(--icon-green)"/>
      <path d="M38 14 V58" stroke="#ffffff" stroke-width="1.5" opacity="0.5"/>
    </svg>
    <div class="area-label">Naturalist<br>intelligence</div>
  </div>
  <div class="area" style="left:594px;top:834px">
    <svg class="area-icon" viewBox="0 0 76 64" role="img" aria-label="Eye icon" style="width:70px">
      <path d="M4 32 Q36 2 70 32 Q36 58 4 32 Z" fill="var(--icon-orange)"/>
      <circle cx="37" cy="31" r="11" fill="#ffffff"/>
      <circle cx="37" cy="31" r="6" fill="var(--icon-orange)"/>
    </svg>
    <div class="area-label">Spatial<br>intelligence</div>
  </div>

  <p class="promo">Enjoy the convenience of ordering online and receiving home delivery<br>or simply stop by our library to borrow our collection of toys</p>

  <footer class="footer">
    <div class="footer-address">2nd Floor, 217 Sunmeadow Arcade, Opp Lotus Bazaar, Amberwood Phase-2, Gurgaon-122017</div>
    <div class="footer-web">www.playvorakids.in</div>
  </footer>
</main>
</body>
</html>
```